Multi-Faceted Legal and Finanacial Advisory Group Needs Business Card Design

We need a business card design for a newly branded Orlando Florida area advising group consisting of Attorneys, Accountants and Financial Planners. The company is named TK Counsel Partners. You will find our initial work on a business card. The information on the business card are merely guideposts and not final product. The logo does not have the be the same as provided since we have not finalized the logo. We would like to stay with a black/white/grey color scheme, but limited use of color is not out of the question.

Target Market(s)

Businesses and their Corporate Representatives

Industry/Entity Type

Business

Contact Information for Business Card

Should have Name, Title, Phone, Cell, Fax, Email and website. Logo should incorporate TK in some fashion however final logo used does not have to be the one on the document provided.

Requirements
Must have
• An TK design on front and back.

```html
<!DOCTYPE html>
<html lang="en">
<head>
<meta charset="utf-8">
<title>TK Counsel Partners – Business Card</title>
<link rel="stylesheet" href="https://fonts.googleapis.com/css2?family=Cormorant+Garamond:wght@500&family=Roboto:wght@300;400&family=Dancing+Script:wght@600&display=swap">
<style>
  :root {
    --backdrop: #dcdcdc;
    --card-dark: #1e1e1e;
    --card-dark-edge: #2b2b2b;
    --card-light: #c4c8cb;
    --card-light-edge: #d4d7d9;
    --ink-light: #f2f2f2;
    --ink-muted: #9a9a9a;
    --ink-dark: #1c1c1c;
    --ink-soft: #3d3d3d;
    --accent: #e3262b;
    --rule: #6f7377;
  }
  * { margin: 0; padding: 0; box-sizing: border-box; }
  html, body { width: 1200px; height: 750px; overflow: hidden; }
  body {
    background: var(--backdrop);
    position: relative;
    font-family: "Roboto", Arial, sans-serif;
  }
  .card {
    position: absolute;
    top: 220px;
    width: 540px;
    height: 310px;
    border-radius: 24px;
    overflow: hidden;
    box-shadow: 0 6px 18px rgba(0,0,0,0.18);
  }
  /* Front */
  .card-front {
    left: 40px;
    background: linear-gradient(135deg, var(--card-dark-edge), var(--card-dark));
  }
  .front-mark {
    position: absolute;
    left: 150px; top: 40px;
    width: 230px; height: 230px;
    background: rgba(255,255,255,0.035);
  }
  .front-name {
    position: absolute;
    left: 0; right: 40px; top: 136px;
    text-align: center;
    font-family: "Cormorant Garamond", Georgia, serif;
    font-weight: 500;
    font-size: 34px;
    font-variant: small-caps;
    letter-spacing: 1px;
    color: var(--ink-light);
  }
  .front-services {
    position: absolute;
    right: -118px; top: 148px;
    transform: rotate(90deg);
    width: 260px;
    text-align: center;
    font-family: "Cormorant Garamond", Georgia, serif;
    font-size: 11px;
    letter-spacing: 1px;
    color: var(--ink-muted);
  }
  /* Back */
  .card-back {
    left: 620px;
    background: linear-gradient(135deg, var(--card-light-edge), var(--card-light));
  }
  .back-brand {
    position: absolute;
    left: 28px; top: 88px;
    width: 150px;
  }
  .brand-name {
    font-family: "Cormorant Garamond", Georgia, serif;
    font-weight: 500;
    font-size: 24px;
    line-height: 1.05;
    font-variant: small-caps;
    color: var(--ink-dark);
  }
  .brand-services {
    margin-top: 14px;
    list-style: none;
    font-family: "Cormorant Garamond", Georgia, serif;
    font-size: 12px;
    line-height: 1.5;
    color: var(--ink-soft);
  }
  .rule {
    position: absolute;
    top: 34px; bottom: 34px;
    width: 0;
  }
  .rule-solid { left: 196px; border-left: 1px solid var(--rule); }
  .rule-dotted { left: 438px; border-left: 1px dotted var(--rule); }
  .back-person {
    position: absolute;
    left: 216px; top: 90px;
    width: 210px;
  }
  .person-name {
    font-size: 38px;
    font-weight: 400;
    color: var(--ink-dark);
    line-height: 1;
  }
  .person-title {
    font-family: "Dancing Script", cursive;
    font-weight: 600;
    font-size: 22px;
    color: var(--accent);
    margin-top: 2px;
  }
  .person-address {
    margin-top: 12px;
    font-style: normal;
    font-size: 10px;
    font-weight: 300;
    line-height: 1.55;
    color: var(--ink-soft);
  }
  .back-phones {
    position: absolute;
    left: 450px; top: 120px;
    list-style: none;
    font-size: 10px;
    font-weight: 300;
    line-height: 1.7;
    color: var(--ink-soft);
    white-space: nowrap;
  }
  .back-phones span { font-weight: 400; }
</style>
</head>
<body>
  <section class="card card-front" aria-label="Card front">
    <div class="front-mark"></div>
    <h1 class="front-name">TK Counsel Partners</h1>
    <p class="front-services">Attorneys · Accountants · Financial Planners</p>
  </section>

  <section class="card card-back" aria-label="Card back">
    <div class="back-brand">
      <p class="brand-name">TK Counsel Partners</p>
      <ul class="brand-services">
        <li>Attorneys</li>
        <li>Accountants</li>
        <li>Financial Planners</li>
      </ul>
    </div>
    <div class="rule rule-solid"></div>
    <div class="back-person">
      <h2 class="person-name">Daniel</h2>
      <p class="person-title">Attorney</p>
      <address class="person-address">
        2480 Lakeview Parkway, Suite 210<br>
        Orlando, FL 32801<br>
        daniel@tkcounselpartners.com<br>
        www.tkcounselpartners.com
      </address>
    </div>
    <div class="rule rule-dotted"></div>
    <ul class="back-phones">
      <li><span>Off</span> (407) 555-0142</li>
      <li><span>Cell</span> (407) 555-0178</li>
      <li><span>Fax</span> (407) 555-0190</li>
    </ul>
  </section>
</body>
</html>
```